14 and Wrens Bar and Grill Menu 2016

Our property is currently going through a renovation to modernize the look and feel of the unit. 14 and Wrens is a restaurant attached to a Dellaway branded hotel in WI and we are making changes as well to provide a gathering place for both guests inside and outside of the hotel.
We need a new menu layout to help attract the local market for our restaurant. We are going for hip and trendy, easy to read, with a layout that is different from the normal fold that is seen everywhere. I have included the logo
Attached is a menu we really like to help give an idea of our style

Target Market(s)

25-45yr old

Industry/Entity Type

American Restaurant

Font styles to use
Other font styles liked:
• Isabel Bold

Colors
1b1b1b
ec1f27
ffffff
d5d5d5

Requirements
Must have
• Must have multiple pages, bold fonts, and easy to change out pages if necessary
• photo on the front for a fun bar and grill type feel
• Menu included with page breaks
Nice to have
• bold headers for each category
• fun tag lines for each category
Should not have
• many pictures aside from the front and back pages of the menu

```html
<!DOCTYPE html>
<html lang="en">
<head>
<meta charset="utf-8">
<title>14 and Wrens Bar and Grill — Menu</title>
<link href="https://fonts.googleapis.com/css2?family=Raleway:wght@300;400;500&display=swap" rel="stylesheet">
<style>
  :root {
    --ink: #1b1b1b;
    --red: #ec1f27;
    --white: #ffffff;
    --rule: #d5d5d5;
    --muted: #8a8a8a;
    --sky-top: #c9d3d8;
    --sky-mid: #bcc8ce;
    --wood: #6b4a33;
    --drink: #a4243a;
    --photo-dark: #1e1d1c;
  }
  * { box-sizing: border-box; margin: 0; padding: 0; }
  html, body { width: 843px; height: 1200px; overflow: hidden; background: var(--white); }
  body { position: relative; font-family: "Raleway", sans-serif; color: var(--ink); }

  /* Cover page */
  .cover {
    position: absolute; left: 86px; top: 70px; width: 304px; height: 720px; overflow: hidden;
  }
  .cover-photo {
    position: absolute; inset: 0;
    background:
      radial-gradient(ellipse 40% 12% at 25% 69%, rgba(164,36,58,.85), transparent 70%),
      radial-gradient(ellipse 30% 12% at 52% 69%, rgba(164,36,58,.85), transparent 70%),
      radial-gradient(ellipse 25% 12% at 85% 68%, rgba(164,36,58,.8), transparent 70%),
      linear-gradient(180deg, var(--sky-top) 0%, var(--sky-mid) 76%, var(--wood) 82%, #4a3526 100%);
  }
  .punch-hole { position: absolute; top: 12px; width: 11px; height: 11px; border-radius: 50%; }
  .cover .punch-hole { background: var(--white); }
  .punch-left { left: 12px; }
  .punch-right { right: 12px; }
  .brand-name {
    position: absolute; left: 0; right: 0; top: 46px; text-align: center;
    font-weight: 300; font-size: 40px; letter-spacing: 1px; color: var(--red);
  }
  .cover-title {
    position: absolute; left: 0; right: 0; text-align: center;
    color: var(--white); font-weight: 300; line-height: 1;
  }
  .title-t { top: 138px; font-size: 108px; }
  .title-he { top: 250px; font-size: 86px; letter-spacing: 10px; padding-left: 10px; }
  .title-menu { top: 380px; font-size: 74px; letter-spacing: 6px; padding-left: 6px; }
  .cover-tag {
    position: absolute; left: 0; right: 0; bottom: 16px; text-align: center;
    color: var(--white); font-weight: 400; font-size: 32px; letter-spacing: 3px;
  }

  /* Appetizer page */
  .page {
    position: absolute; left: 453px; top: 70px; width: 302px; height: 720px;
    border: 1px solid var(--ink); background: var(--white);
  }
  .page .punch-hole { background: var(--ink); top: 8px; }
  .page .punch-left { left: 9px; }
  .page .punch-right { right: 9px; }
  .page-frame {
    position: absolute; left: 8px; right: 8px; top: 28px; bottom: 12px;
    border: 5px solid #e6e6e6;
  }
  .page-frame::after {
    content: ""; position: absolute; inset: 3px; border: 1px solid #e6e6e6;
  }
  .menu-list {
    position: absolute; left: 0; right: 0; top: 50px; text-align: center;
  }
  .menu-item { margin-bottom: 14px; }
  .item-name { font-size: 12.5px; font-weight: 400; letter-spacing: -0.3px; line-height: 15px; }
  .item-desc { font-size: 12px; font-weight: 300; color: var(--muted); line-height: 14.7px; }
  .service-note {
    position: absolute; left: 0; right: 0; top: 618px; text-align: center;
    font-size: 9.5px; font-weight: 300; color: var(--muted); line-height: 14.5px;
  }
  .section-title {
    position: absolute; left: 50%; transform: translateX(-50%); bottom: 6px;
    background: var(--white); padding: 0 12px;
    font-size: 24px; font-weight: 500; letter-spacing: 4px; white-space: nowrap;
  }

  /* Presentation photo */
  .holder-photo {
    position: absolute; left: 315px; top: 811px; width: 213px; height: 317px;
    background: radial-gradient(ellipse 45% 55% at 55% 50%, #efe8d6 0%, #d9cfb8 40%, #3a3430 70%, var(--photo-dark) 100%);
  }
</style>
</head>
<body>

  <section class="cover">
    <div class="cover-photo" role="img" aria-label="Photo of three red crushed-ice cocktails garnished with berries and apple on a wooden crate"></div>
    <span class="punch-hole punch-left"></span>
    <span class="punch-hole punch-right"></span>
    <div class="brand-name">14 and Wrens</div>
    <div class="cover-title title-t">T</div>
    <div class="cover-title title-he">HE</div>
    <div class="cover-title title-menu">MENU</div>
    <div class="cover-tag">BAR AND GRILL</div>
  </section>

  <section class="page">
    <span class="punch-hole punch-left"></span>
    <span class="punch-hole punch-right"></span>
    <div class="page-frame"></div>
    <div class="menu-list">
      <div class="menu-item">
        <div class="item-name">BRUSCHETTA 9</div>
        <div class="item-desc">tomato, basil, garlic, olive oil,<br>parmesan cheese,<br>parmesan crostinis | w/shrimp 14</div>
      </div>
      <div class="menu-item">
        <div class="item-name">SPINACH &amp; ARTICHOKE DIP 9</div>
        <div class="item-desc">spinach, artichoke, parmesan, garlic,<br>house-made, crispy tortilla chips</div>
      </div>
      <div class="menu-item">
        <div class="item-name">CRUNCHY CHICKEN FINGERS 10</div>
        <div class="item-desc">hand breaded, deep fried</div>
      </div>
      <div class="menu-item">
        <div class="item-name">SMOKED WINGS 11</div>
        <div class="item-desc">buffalo, barbecue, szechwan or en fuego<br>boneless 10 | traditional 11</div>
      </div>
      <div class="menu-item">
        <div class="item-name">CHICKEN NACHOS 11</div>
        <div class="item-desc">grilled chicken, queso, black beans,<br>jalapeño, cilantro,<br>pico de gallo, guacamole,<br>sour cream, tortilla chips</div>
      </div>
      <div class="menu-item">
        <div class="item-name">ROASTED VEGETABLE FLATBREAD 11</div>
        <div class="item-desc">fresh spinach &amp; artichoke sauce,<br>tomato, mushrooms, basil,<br>balsamic onions, mozzarella<br>and provolone cheese blend</div>
      </div>
      <div class="menu-item">
        <div class="item-name">BUFFALO CHICKEN FLATBREAD 11.50</div>
        <div class="item-desc">grilled chicken, green onion, blue cheese<br>crumbles, buffalo sauce,<br>smoked onion ranch, mozzarella<br>and provolone cheese blend</div>
      </div>
    </div>
    <p class="service-note">An 18% service charge will be added<br>to all purchases for parties of 8 or more.</p>
    <h2 class="section-title">APPETIZERS</h2>
  </section>

  <div class="holder-photo" role="img" aria-label="Photo of hands flipping cream menu pages clipped to a dark wooden board"></div>

</body>
</html>
```